[AMAZING DESIGN NEEDED] Women's Fishing Squeeze Page

I need a professional design for a landing page that is going to collect email addresses.

You can use the creatives already on the page or you can pull images from the facebook/instagram pages.
https://www.facebook.com/LakesLuresBoots
https://www.instagram.com/lakesluresandboots/

This is the page that needs designed: https://lakesluresandboots.example/email-opt-in/

See attached for examples.

Target Market(s)

Women who like to go fishing

Industry/Entity Type

Fishing

Number of Pages Required

1 page

Font styles to use
Sans Serif

Requirements
Must have
• excellent design. Call to actions.

```html
<!DOCTYPE html>
<html lang="en">
<head>
<meta charset="utf-8">
<title>Lakes, Lures &amp; Boots — Sign Up</title>
<link href="https://fonts.googleapis.com/css2?family=Roboto:wght@400;500&family=IBM+Plex+Sans:wght@400;700&family=Dancing+Script:wght@500&family=Volkhov&display=swap" rel="stylesheet">
<style>
:root{
  --sand:#c4b09d;
  --maroon:#5a2d2e;
  --ink:#4a3a33;
  --link:#7b5f52;
  --accent:#c6ab93;
  --dark-btn:#3e2a24;
  --panel:rgba(255,255,255,.86);
}
*{box-sizing:border-box;margin:0;padding:0}
html,body{width:1088px;height:1200px;overflow:hidden}
body{background:var(--sand);font-family:"Roboto",sans-serif;color:var(--ink);position:relative}
a{color:inherit;text-decoration:none}
.abs{position:absolute}

.top-bar{top:17px;left:617px;display:flex;align-items:center;gap:9px;font-size:10px;font-weight:500;color:var(--ink);text-transform:uppercase}
.social-square{width:15px;height:15px;background:var(--ink);border-radius:2px;display:block}
.top-bar .divider{width:1px;height:14px;background:var(--ink);margin:0 2px}
.top-bar .links{display:flex;gap:15px}
.top-bar .or{text-transform:none;font-weight:400}

.brand{top:48px;left:486px;width:130px;height:118px;display:flex;flex-direction:column;align-items:center;justify-content:center;gap:8px;font-family:"Volkhov",serif;color:var(--maroon);text-align:center}
.brand-circle{width:16px;height:16px;border-radius:50%;background:var(--maroon)}
.brand-name{font-size:13px;letter-spacing:2px;line-height:1.4}

.main-nav{top:190px;left:0;width:100%;display:flex;justify-content:center;gap:23px;font-size:10.5px;font-weight:500;color:var(--ink);text-transform:uppercase}
.main-nav .caret{font-size:8px;margin-left:5px}

.hero{top:223px;left:0;width:1088px;height:622px;background:linear-gradient(180deg,#7fa6d6 0%,#b9c9dc 10%,#6d7f5b 22%,#3f5a34 38%,#5a7a88 52%,#3f6b7c 68%,#7d8b86 86%,#9a8f82 100%)}
.signup-panel{top:263px;left:548px;width:421px;height:523px;background:var(--panel);font-family:"IBM Plex Sans",sans-serif;text-align:center}
.signup-title{position:absolute;top:36px;left:0;width:100%;font-size:46px;font-weight:700;color:#111;letter-spacing:.5px;white-space:nowrap}
.signup-title .script{font-family:"Dancing Script",cursive;font-weight:500;font-size:48px;margin-left:8px}
.offer{position:absolute;top:120px;left:0;width:100%;font-size:30px;line-height:45px;color:#111}
.offer .badge{background:var(--accent);color:#fff;font-weight:700;padding:0 7px}
.field{position:absolute;left:42px;width:341px;height:49px;background:#fff;border:1px solid #cfc8c2;font-size:13px;color:#333;padding:0 16px;display:flex;align-items:center}
.field .req{color:#c0392b;margin-left:4px}
.subscribe-btn{position:absolute;left:42px;top:430px;width:341px;height:54px;background:var(--maroon);color:#fff;font-size:18px;font-weight:700;letter-spacing:.5px;display:flex;align-items:center;justify-content:center}

.connect{top:871px;left:875px;font-family:"Volkhov",serif;font-size:11px;color:var(--ink)}
.connect-icons{top:903px;left:919px;display:flex;gap:11px}

.footer-col{top:959px;font-size:10px;line-height:15.2px;color:var(--link)}
.footer-col h4{font-family:"Volkhov",serif;font-weight:400;font-size:11px;color:var(--ink);margin-bottom:8px}
.footer-col .muted{font-style:italic}
.footer-col .phone{font-weight:500}
.newsletter-form{top:1028px;left:563px;display:flex;gap:8px}
.newsletter-form .email{width:156px;height:30px;background:#fff;border:1px solid #bfb2a5;border-radius:3px;font-size:10px;color:#444;padding:0 10px;display:flex;align-items:center}
.newsletter-form .btn{width:96px;height:30px;background:var(--dark-btn);color:#fff;border-radius:3px;font-family:"Volkhov",serif;font-size:10.5px;display:flex;align-items:center;justify-content:center}
.payments{top:1117px;left:567px;display:flex;gap:12px;align-items:center}
.payments span{display:block;width:36px;height:17px;background:#8d7466;border-radius:3px}
.copyright{top:1170px;left:150px;font-size:8.5px;color:var(--ink)}
</style>
</head>
<body>

<header>
  <div class="abs top-bar">
    <a class="social-square" href="#" aria-label="Our social page"></a>
    <a class="social-square" href="#" aria-label="Our photo feed"></a>
    <span class="divider"></span>
    <nav class="links">
      <a href="#">Search</a>
      <a href="#">Gift Certificates</a>
      <a href="#">Sign in <span class="or">or</span> Register</a>
      <a href="#">Cart</a>
    </nav>
  </div>

  <a class="abs brand" href="https://lakesluresandboots.example/">
    <span class="brand-circle"></span>
    <span class="brand-name">LAKES, LURES<br>&amp; BOOTS</span>
  </a>

  <nav class="abs main-nav">
    <a href="#">Clothing<span class="caret">&#9013;</span></a>
    <a href="#">Hats</a>
    <a href="#">Bundles</a>
    <a href="#">Accessories &amp; Stickers</a>
    <a href="#">Jewelry</a>
    <a href="#">Clearance</a>
  </nav>
</header>

<main>
  <div class="abs hero" role="img" aria-label="Photo of a woman fly fishing at the edge of a clear mountain lake with forested slopes and blue sky"></div>

  <section class="abs signup-panel">
    <h1 class="signup-title">SIGN UP<span class="script">Today</span></h1>
    <p class="offer">And Receive <span class="badge">15% Off</span><br>Your Next Order</p>
    <div class="field" style="top:245px">First Name</div>
    <div class="field" style="top:304px">Last Name</div>
    <div class="field" style="top:364px">Email Address<span class="req">*</span></div>
    <a class="subscribe-btn" href="#">SUBSCRIBE AND SAVE</a>
  </section>
</main>

<footer>
  <div class="abs connect">Connect With Us</div>
  <div class="abs connect-icons">
    <a class="social-square" href="#" aria-label="Our social page"></a>
    <a class="social-square" href="#" aria-label="Our photo feed"></a>
  </div>

  <div class="abs footer-col" style="left:150px">
    <h4>Navigate</h4>
    <a href="#">Trips</a><br><a href="#">Shipping &amp; Returns</a><br><a href="#">Contact Us</a><br><a href="#">Blog</a><br><a href="#">Sitemap</a>
  </div>
  <div class="abs footer-col" style="left:288px">
    <h4>Categories</h4>
    <a href="#">Clothing</a><br><a href="#">Hats</a><br><a href="#">Bundles</a><br><a href="#">Accessories &amp; Stickers</a><br><a href="#">Jewelry</a><br><a href="#">Clearance</a>
  </div>
  <div class="abs footer-col" style="left:425px">
    <h4>Info</h4>
    <span class="muted">Montana</span><br><span class="phone">Call us at 4065550142</span>
  </div>
  <div class="abs footer-col" style="left:563px;width:250px">
    <h4>Subscribe to our newsletter</h4>
    Get the latest updates on new products and upcoming sales
  </div>
  <div class="abs newsletter-form">
    <div class="email">Your email address</div>
    <a class="btn" href="#">Subscribe</a>
  </div>

  <div class="abs payments" aria-label="Accepted payment methods">
    <span></span><span></span><span></span><span></span><span></span>
  </div>

  <div class="abs copyright">© 2021 Lakes, Lures &amp; Boots</div>
</footer>

</body>
</html>
```